Packaging Design Project for a Pet Product Company

Need a packaging design for a pet product company based in Los Angeles. We offer user-friendly pet products to people. This new product is a Collapsible Pet Bowl that folds in 4 ways for dogs of all sizes. It can be used for food or water. It is light-weight, functional and eco-friendly. Great for indoor/outdoor use at home and it's easy to take on the go.

www.tuftmeadow.com - get the look and feel of our design.
(This project is for a new bowl which is not yet announced on our website.)

I can be reached via the SketchHive comment board or at rilo481@mailvendo.com.

Target Market(s)

Pet boutique owners and customers

Industry/Entity Type

It Company

Requirements
Must have
• Use kraft paper as the background color of the design

Maintain a Modern, fun, creative and eco-friendly look in the design

color scheme:
Background color: kraft paper
Design & Font color: WHITE and CHARCOAL GREY are must. Possibly a 3rd color (Tuft Meadow logo green or any 3rd color of your choice)

Maintain consistency with our "existing packaging for current product line" (see attached file)

Picture of a Labradoodle dog with a bowl in front of the dog (black and white)
Nice to have
• Play around with the composition/layout of the design and suggest any creative touch to make it better

Modify the wording/content if necessary

Mock-up rendering should be as realistic as possible

Use one of our bowl color in mock-up rendering. Same packaging for pink bowl and the green bowl.

```html
<!DOCTYPE html>
<html lang="en">
<head>
<meta charset="utf-8">
<title>Tuft Meadow – Collapsible Pet Bowl Packaging</title>
<link href="https://fonts.googleapis.com/css2?family=Comic+Neue:wght@400;700&display=swap" rel="stylesheet">
<style>
  :root {
    --backdrop: #e4e4e6;
    --kraft: #ead8b1;
    --kraft-deep: #dcc597;
    --charcoal: #4a4541;
    --ink-soft: #6b625a;
    --fold-green: #a8bd8e;
    --fold-pink: #e4a4ac;
    --box-tint: #dcc69a;
    --white: #ffffff;
  }
  * { box-sizing: border-box; margin: 0; padding: 0; }
  html, body { width: 1200px; height: 900px; overflow: hidden; }
  body {
    background: var(--backdrop);
    font-family: "Comic Neue", sans-serif;
    color: var(--charcoal);
    position: relative;
  }
  .dieline { position: absolute; left: 0; top: 0; }
  .abs { position: absolute; text-align: center; }
  .brand {
    font-weight: 700; font-size: 27px; letter-spacing: 0.5px;
    display: flex; align-items: center; justify-content: center; gap: 9px;
  }
  .brand-mark { width: 26px; height: 26px; border-radius: 50%; background: var(--charcoal); }
  .url { font-weight: 700; font-size: 19px; }
  .title-small { font-weight: 700; font-size: 25px; }
  .title-large { font-weight: 700; font-size: 40px; }
  .front-claims { font-weight: 700; font-size: 14px; line-height: 16px; }
  .back-title { font-weight: 700; font-size: 20px; }
  .fold-note { font-weight: 700; font-size: 8.5px; line-height: 10px; text-align: left; }
  .feature-box {
    background: var(--box-tint);
    font-weight: 700; font-size: 11px; line-height: 18px;
    display: flex; flex-direction: column; justify-content: center; align-items: center;
  }
  .spec-list { font-weight: 700; font-size: 8.5px; line-height: 10px; text-align: left; }
  .upc-box {
    background: var(--white);
    display: flex; align-items: center; justify-content: center;
    font-size: 19px; color: var(--charcoal);
  }
</style>
</head>
<body>

<svg class="dieline" width="1200" height="900" viewBox="0 0 1200 900">
  <defs>
    <linearGradient id="pupTone" x1="0" y1="0" x2="0" y2="1">
      <stop offset="0" stop-color="#2a2420"/>
      <stop offset="0.6" stop-color="#3a2c22"/>
      <stop offset="1" stop-color="#8a5a34"/>
    </linearGradient>
    <linearGradient id="bowlTone" x1="0" y1="0" x2="0" y2="1">
      <stop offset="0" stop-color="#8a8079"/>
      <stop offset="1" stop-color="#6e655e"/>
    </linearGradient>
  </defs>

  <!-- Front panel -->
  <g class="front-panel">
    <rect x="307" y="19" width="229" height="808" fill="var(--kraft)"/>
    <circle cx="421" cy="480" r="173" fill="var(--kraft)"/>
    <path d="M307 827 L536 827 L536 836 L527 843 L527 880 L316 880 L316 843 L307 836 Z" fill="var(--kraft)"/>
    <path d="M373 65 Q373 58 380 58 L396 58 Q403 49 410 58 L426 58 Q433 58 433 65 Q433 72 426 72 L380 72 Q373 72 373 65 Z" fill="none" stroke="var(--fold-pink)" stroke-width="1.3"/>
    <line x1="307" y1="191" x2="536" y2="191" stroke="var(--fold-green)" stroke-width="1"/>
    <line x1="307" y1="243" x2="536" y2="243" stroke="var(--fold-green)" stroke-width="1"/>
    <line x1="307" y1="720" x2="536" y2="720" stroke="var(--fold-green)" stroke-width="1"/>
    <line x1="307" y1="773" x2="536" y2="773" stroke="var(--fold-green)" stroke-width="1"/>
    <line x1="307" y1="827" x2="536" y2="827" stroke="var(--fold-green)" stroke-width="1"/>
    <circle cx="421" cy="480" r="118" fill="none" stroke="var(--kraft-deep)" stroke-width="5"/>
    <circle cx="421" cy="480" r="100" fill="none" stroke="var(--kraft-deep)" stroke-width="3"/>
    <g role="img" aria-label="Scattered paw print decorations around the badge">
      <circle cx="300" cy="393" r="13" fill="var(--kraft-deep)"/>
      <circle cx="283" cy="473" r="14" fill="var(--kraft-deep)"/>
      <circle cx="297" cy="545" r="13" fill="var(--kraft-deep)"/>
      <circle cx="555" cy="440" r="13" fill="var(--kraft-deep)"/>
      <circle cx="555" cy="532" r="14" fill="var(--kraft-deep)"/>
    </g>
    <rect x="330" y="372" width="160" height="222" rx="30" fill="url(#pupTone)" role="img" aria-label="Photo of a sitting tricolour puppy"/>
    <rect x="380" y="632" width="84" height="18" rx="6" fill="url(#bowlTone)" role="img" aria-label="Four bowl heights shown side by side"/>
    <g class="care-icons" fill="none" stroke="var(--charcoal)" stroke-width="1.5">
      <circle cx="333" cy="800" r="13"/>
      <line x1="333" y1="792" x2="333" y2="806"/><circle cx="333" cy="807" r="2"/>
      <circle cx="364" cy="800" r="13"/>
      <path d="M359 793 L359 807 M369 793 Q372 800 369 803 L369 807"/>
      <circle cx="461" cy="800" r="13"/>
      <rect x="454" y="794" width="14" height="11" rx="1"/>
      <circle cx="492" cy="800" r="13"/>
      <rect x="485" y="793" width="14" height="13" rx="1"/><line x1="485" y1="797" x2="499" y2="797"/>
    </g>
  </g>

  <!-- Back panel -->
  <g class="back-panel">
    <rect x="692" y="19" width="228" height="690" fill="var(--kraft)"/>
    <path d="M757 65 Q757 58 764 58 L780 58 Q787 49 794 58 L810 58 Q817 58 817 65 Q817 72 810 72 L764 72 Q757 72 757 65 Z" fill="none" stroke="var(--fold-pink)" stroke-width="1.3"/>
    <line x1="692" y1="187" x2="920" y2="187" stroke="var(--fold-green)" stroke-width="1"/>
    <line x1="692" y1="240" x2="920" y2="240" stroke="var(--fold-green)" stroke-width="1"/>
    <path d="M763 317 L763 349 M759 321 L763 316 L767 321 M759 345 L763 350 L767 345" fill="none" stroke="var(--charcoal)" stroke-width="1"/>
    <g role="img" aria-label="Collapsed and expanded bowl illustration">
      <ellipse cx="800" cy="330" rx="30" ry="12" fill="url(#bowlTone)"/>
      <rect x="822" y="340" width="74" height="58" rx="14" fill="url(#bowlTone)"/>
    </g>
  </g>
</svg>

<!-- Front panel text -->
<div class="abs brand" style="left:307px;top:116px;width:229px;">
  <span class="brand-mark"></span><span>Tuft Meadow</span>
</div>
<div class="abs url" style="left:307px;top:204px;width:229px;">www.tuftmeadow.com</div>
<div class="abs title-small" style="left:307px;top:266px;width:229px;">Collapsible</div>
<div class="abs title-large" style="left:307px;top:296px;width:229px;">Pet Bowl</div>
<div class="abs front-claims" style="left:307px;top:663px;width:229px;">
  100% Silicone<br>Adjustable to 4 different sizes<br>it's like having 4 bowls in one!
</div>

<!-- Back panel text -->
<div class="abs brand" style="left:692px;top:116px;width:228px;">
  <span class="brand-mark"></span><span>Tuft Meadow</span>
</div>
<div class="abs url" style="left:692px;top:201px;width:228px;">www.tuftmeadow.com</div>
<div class="abs back-title" style="left:692px;top:272px;width:228px;">Collapsible Pet Bowl</div>
<div class="abs fold-note" style="left:711px;top:322px;width:45px;">Fold down<br>to only<br>1.5 inches</div>
<div class="abs feature-box" style="left:713px;top:420px;width:190px;height:56px;">
  <span>• Adjustable to 4 different sizes</span>
  <span>• Easy to clean</span>
  <span>• Non-slip design</span>
</div>
<div class="abs feature-box" style="left:713px;top:493px;width:190px;height:124px;line-height:14px;gap:4px;">
  <span>• Lightweight, Functional and<br>Eco-friendly</span>
  <span>• For dogs of all sizes</span>
  <span>• No splattered mess</span>
  <span>• Use for food or water</span>
  <span>• Great for indoor/outdoor use at<br>home and easy to take on the go</span>
</div>
<div class="abs spec-list" style="left:713px;top:628px;width:125px;">
  64 oz. / 8 cups Capacity<br>Fold down to only 1.5 inches<br>100% Food Grade Silicone<br>Dishwasher Safe (Top Rack)<br>FDA Food-Safe Silicone
</div>
<div class="abs upc-box" style="left:840px;top:627px;width:63px;height:64px;">UPC</div>

</body>
</html>
```